Online Car Options Brochure

I need an online product brochure that list basic information, price and options for a new sports car. brochure can be in either PDF or any other form that is easy to download or view on a website. this is for online viewing so not a trifold but can be multiple full pages.
the product will launch in 2 weeks. I have attached logo, basic highlights and pricing and options list. because car has not yet been launched I will not include pictures of the car yet for privacy. I will send pictures of the car to be included in the brochure once the design is awarded to be placed in the brochure so please leave space for a few pictures. the purpose of the brochure is to provide basic highlights of the car, pricing and options breakdown. more detailed information is available on the website. I prefer a clean, simple brochure for an upscale taste. primary colors of the website are black, silver, grey high tech look. logo is red. please email me with any questions. thx

```html
<!DOCTYPE html>
<html lang="en">
<head>
<meta charset="utf-8">
<title>Options – Price List Spread</title>
<link href="https://fonts.googleapis.com/css2?family=Oswald:wght@300;400&family=Orbitron:wght@400&display=swap" rel="stylesheet">
<style>
  :root{
    --stage-light:#d9d9d9;
    --stage-dark:#8c8c8c;
    --spread-dark:#2e2a29;
    --photo-warm:#b9814f;
    --photo-deep:#6b4a33;
    --text:#f2eeea;
    --rule:rgba(20,18,18,.75);
    --fold:rgba(255,255,255,.35);
  }
  *{margin:0;padding:0;box-sizing:border-box}
  html,body{width:1200px;height:1000px;overflow:hidden}
  body{
    background:radial-gradient(ellipse 70% 60% at 50% 45%,var(--stage-light),var(--stage-dark));
    position:relative;
    font-family:"Oswald",sans-serif;
    font-weight:300;
    color:var(--text);
  }
  .spread{
    position:absolute;left:12px;top:197px;width:1176px;height:621px;
    background:var(--spread-dark);overflow:hidden;
  }
  .spread-photo{
    position:absolute;inset:0;
    background:
      radial-gradient(ellipse 45% 40% at 50% 62%,var(--photo-warm),transparent 70%),
      radial-gradient(ellipse 70% 55% at 50% 55%,var(--photo-deep),transparent 80%),
      linear-gradient(180deg,#3b3634 0%,#4a3a30 45%,#3a2f2a 80%,#2c2827 100%);
  }
  .spread-shade{position:absolute;inset:0;background:rgba(30,26,25,.35)}
  .fold{position:absolute;left:588px;top:0;width:1px;height:100%;background:var(--fold)}
  .page{position:absolute;top:0;height:100%}
  .page-left{left:54px;width:481px}
  .page-right{left:643px;width:480px}
  .page-title{
    font-family:"Orbitron",sans-serif;font-weight:400;font-size:14.5px;
    letter-spacing:.5px;position:absolute;top:56px;left:6px;
  }
  .options-table{
    position:absolute;top:76px;left:0;width:100%;
    border-collapse:collapse;font-size:10.5px;text-transform:uppercase;line-height:13px;
  }
  .options-table td{
    border-bottom:1px solid var(--rule);height:22px;vertical-align:top;padding:4px 6px 0;
  }
  .options-table td + td{border-left:1px solid var(--rule)}
  .options-table tr:first-child td{border-top:1px solid var(--rule)}
  .options-table .tall td{height:38px}
  .options-table .tall-26 td{height:26px;padding-top:6px}
  .cat{text-align:left}
  .item{text-align:center}
  .status{text-align:center}
  .price{text-align:right}
  .page-left .cat{width:144px}.page-left .item{width:206px}.page-left .status{width:71px}
  .page-right .cat{width:143px}.page-right .item{width:207px}.page-right .status{width:70px}
  .terms{position:absolute;top:440px;left:6px;width:470px;font-size:6.3px;text-transform:uppercase;line-height:9.5px}
  .schedule{display:flex}
  .schedule-label{width:160px}
  .schedule-lines{text-align:center;width:130px}
  .footnote{margin-top:14px}
  .payment-terms{margin-top:10px}
</style>
</head>
<body>
<section class="spread">
  <div class="spread-photo" role="img" aria-label="Full-bleed photograph of an orange sports car seen head-on, darkened behind the price tables"></div>
  <div class="spread-shade"></div>
  <div class="fold"></div>

  <div class="page page-left">
    <h2 class="page-title">OPTIONS</h2>
    <table class="options-table">
      <tr><td class="cat">Suspension System</td><td class="item">Tuned Non-Adjustable Dampers</td><td class="status">Standard</td><td class="price">0,00</td></tr>
      <tr class="tall-26"><td class="cat"></td><td class="item">Veltra Aluminum Adjustable Dampers</td><td class="status">Option</td><td class="price">2.720,00</td></tr>
      <tr><td></td><td></td><td></td><td></td></tr>
      <tr><td class="cat">Steering System</td><td class="item">Quick Release Steering Wheel Hub</td><td class="status">Option</td><td class="price">275,00</td></tr>
      <tr><td></td><td></td><td></td><td></td></tr>
      <tr><td class="cat">Seating</td><td class="item">One-Piece Fiberglass Bucket</td><td class="status">Standard</td><td class="price">0,00</td></tr>
      <tr><td class="cat"></td><td class="item">Premium Leather Racing Seats</td><td class="status">Option</td><td class="price">1.499,00</td></tr>
      <tr><td></td><td></td><td></td><td></td></tr>
      <tr><td class="cat">Seats Belts</td><td class="item">2 Inch 4 Point Harness</td><td class="status">Standard</td><td class="price">0,00</td></tr>
      <tr><td class="cat"></td><td class="item">3 Inch 4 Point Harness</td><td class="status">Option</td><td class="price">328,00</td></tr>
      <tr><td class="cat"></td><td class="item">HRD Specific Shoulder Belts</td><td class="status">Option</td><td class="price">422,32</td></tr>
      <tr><td class="cat"></td><td class="item">Anti-Sub Belt</td><td class="status">Option</td><td class="price">49,33</td></tr>
      <tr><td class="cat"></td><td class="item">Seat Belt Pads</td><td class="status">Option</td><td class="price">37,29</td></tr>
      <tr><td></td><td></td><td></td><td></td></tr>
      <tr><td class="cat">Screens</td><td class="item">Standard Screen (No Deflector</td><td class="status">Standard</td><td class="price">0,00</td></tr>
      <tr><td class="cat"></td><td class="item">Aero Screens</td><td class="status">Option</td><td class="price">146,85</td></tr>
      <tr><td class="cat"></td><td class="item">Full Glass Windscreen Package</td><td class="status">Option</td><td class="price">2.850,00</td></tr>
      <tr><td></td><td></td><td></td><td></td></tr>
      <tr class="tall"><td class="cat">Body Work/ Appearance</td><td class="item">Chassis Powder Coat(Grey/Black/ Gunmetal)</td><td class="status">Standard</td><td class="price">0,00</td></tr>
      <tr class="tall"><td class="cat"></td><td class="item">Premium Dash, Steering Wheel Covered in Leather Trim</td><td class="status">Option</td><td class="price">4.999,00</td></tr>
    </table>
  </div>

  <div class="page page-right">
    <h2 class="page-title">OPTIONS</h2>
    <table class="options-table">
      <tr><td class="cat">Track Day Options</td><td class="item">Battery Master Switch</td><td class="status">Option</td><td class="price">275,00</td></tr>
      <tr><td class="cat"></td><td class="item">Roll Bar Hoop</td><td class="status">Option</td><td class="price">990,00</td></tr>
      <tr><td class="cat"></td><td class="item">Fire Extinguisher Kit</td><td class="status">Option</td><td class="price">675,00</td></tr>
      <tr><td class="cat"></td><td class="item">Tracklog Data Logger</td><td class="status">Option</td><td class="price">1.200,00</td></tr>
      <tr><td></td><td></td><td></td><td></td></tr>
      <tr class="tall"><td class="cat">Wheels/Tires</td><td class="item">Front 18" Forged Aluminum 245/40/18 Tarmac R900</td><td class="status">Standard</td><td class="price">0,00</td></tr>
      <tr class="tall"><td class="cat"></td><td class="item">Rear 19" Forged Aluminum 295/35/19 Tarmac R900</td><td class="status">Standard</td><td class="price">0,00</td></tr>
      <tr><td></td><td></td><td></td><td></td></tr>
      <tr><td class="cat">Misc. Options</td><td class="item">Car Cover - Indoor</td><td class="status">Option</td><td class="price">525,00</td></tr>
      <tr><td class="cat"></td><td class="item">Car Cover - Outdoor</td><td class="status">Option</td><td class="price">525,00</td></tr>
      <tr><td class="cat"></td><td class="item">Passenger Footrest</td><td class="status">Option</td><td class="price">197,35</td></tr>
      <tr><td class="cat"></td><td class="item">Road Race Lighting Kit</td><td class="status">Option</td><td class="price">1.358,37</td></tr>
      <tr><td class="cat"></td><td class="item">12V Power Source</td><td class="status">Option</td><td class="price">66,00</td></tr>
      <tr><td class="cat"></td><td class="item">Locking Fuel Cap</td><td class="status">Option</td><td class="price">75,00</td></tr>
      <tr><td></td><td></td><td></td><td></td></tr>
    </table>

    <div class="terms">
      <div class="schedule">
        <div class="schedule-label">Payment Schedule:</div>
        <div class="schedule-lines">50% due at the time of order<br>40% due at final assembly<br>10% due at delivery</div>
      </div>
      <p class="footnote">* The Vantor Apex is not sold directly by Kestrel Motors. The Apex can either be sourced by clients or we can help source it for you. The Raptor™<br>retains most components of the Apex except lights, body work, wheels and tires.</p>
      <p class="payment-terms">Payment terms:<br>All payments are non-refundable<br>All orders are entered within the build queue based on initial deposit receipt</p>
    </div>
  </div>
</section>
</body>
</html>
```